Banner for construction site to identify developer

we need a 4 foot by 8 foot banner to hang on the fence of a residential townhome development in Phoenix, Arizona that identifies Tolvane Holdings as the company behind the development/project. Also needs to include the logo, phone number, and web address. Would like to stick with the blue colors provided in the attached logo. The blues should stay the same but the letters in the logo can change to another color if necessary. Feel free to use "Tolvane Holdings" in place of "Tolvane Holdings Group". Looking for use of colors/design to take up space so banner is not just text with a logo.

Target Market(s)

drive by traffic looking at the site

Industry/Entity Type

Real Estate

Colors
0054AA
0677BA
7BADD7
CADEEF
E8F1F8

Requirements
Must have
• company name, phone number and web address

```html
<!DOCTYPE html>
<html lang="en">
<head>
<meta charset="utf-8">
<title>Tolvane Holdings – Site Banner</title>
<link rel="stylesheet" href="https://fonts.googleapis.com/css2?family=Montserrat:wght@700&family=Open+Sans:wght@800&display=swap">
<style>
  :root {
    --page-bg: #e8e8e8;
    --frame: #ffffff;
    --navy: #404f72;
    --navy-deep: #2e3a58;
    --sky: #2ca6dc;
    --ocean: #1a6fa3;
    --white: #ffffff;
  }
  html, body {
    margin: 0;
    width: 1200px;
    height: 678px;
    overflow: hidden;
    background: var(--page-bg);
  }
  .banner {
    position: absolute;
    left: 30px;
    top: 40px;
    width: 1084px;
    height: 541px;
    border: 28px solid var(--frame);
    background: var(--navy);
    overflow: hidden;
  }
  .hero {
    position: absolute;
    left: 0; top: 0;
    width: 1084px;
    height: 397px;
    background: var(--navy);
  }
  .hero-shade {
    position: absolute;
    left: 0; top: 0;
  }
  .hero-floor {
    position: absolute;
    left: 0; bottom: 0;
    width: 100%;
    height: 75px;
    background: linear-gradient(to bottom, rgba(46,58,88,0) 0%, rgba(30,38,62,0.75) 100%);
  }
  .skyline {
    position: absolute;
    left: 680px;
    top: 30px;
    width: 360px;
    height: 293px;
    background: linear-gradient(to bottom, rgba(220,228,240,0.85) 0%, rgba(160,176,204,0.55) 60%, rgba(64,79,114,0.1) 100%);
  }
  .brand {
    position: absolute;
    left: 113px;
    top: 218px;
    display: flex;
    align-items: flex-end;
    gap: 18px;
  }
  .brand-mark {
    width: 70px;
    height: 70px;
    background: var(--sky);
    margin-bottom: 12px;
  }
  .brand-name {
    font-family: "Open Sans", sans-serif;
    font-weight: 800;
    font-size: 80px;
    line-height: 1;
    color: var(--white);
    letter-spacing: -1px;
    white-space: nowrap;
  }
  .accent-stripe {
    position: absolute;
    left: 0; top: 397px;
    width: 100%;
    height: 12px;
    background: var(--sky);
  }
  .contact-bar {
    position: absolute;
    left: 0; top: 409px;
    width: 100%;
    height: 132px;
    background: var(--ocean);
    display: flex;
    align-items: center;
    justify-content: center;
    gap: 56px;
    font-family: "Montserrat", sans-serif;
    font-weight: 700;
    font-size: 34px;
    color: var(--white);
  }
  .contact-item {
    display: flex;
    align-items: center;
    gap: 18px;
    white-space: nowrap;
  }
  .contact-icon { display: block; }
</style>
</head>
<body>
  <main class="banner">
    <section class="hero">
      <svg class="hero-shade" width="1084" height="397" viewBox="0 0 1084 397" aria-hidden="true">
        <polygon points="535,75 1084,75 1084,323 850,323" fill="var(--navy-deep)" opacity="0.6"/>
      </svg>
      <div class="skyline" role="img" aria-label="Illustration of a city skyline with lit office towers"></div>
      <div class="hero-floor"></div>
      <div class="brand">
        <div class="brand-mark"></div>
        <h1 class="brand-name">Tolvane Holdings</h1>
      </div>
    </section>
    <div class="accent-stripe"></div>
    <footer class="contact-bar">
      <div class="contact-item">
        <svg class="contact-icon" width="43" height="43" viewBox="0 0 44 44" aria-hidden="true">
          <g fill="none" stroke="var(--white)" stroke-width="4">
            <circle cx="22" cy="22" r="19"/>
            <ellipse cx="22" cy="22" rx="8" ry="19"/>
            <line x1="3" y1="22" x2="41" y2="22"/>
          </g>
        </svg>
        <span class="contact-web">tolvaneholdingsgroup.com</span>
      </div>
      <div class="contact-item">
        <svg class="contact-icon" width="34" height="36" viewBox="0 0 24 24" aria-hidden="true">
          <path fill="var(--white)" d="M6.6 10.8c1.4 2.8 3.8 5.1 6.6 6.6l2.2-2.2c.3-.3.7-.4 1-.2 1.1.4 2.3.6 3.6.6.6 0 1 .4 1 1V20c0 .6-.4 1-1 1C10.6 21 3 13.4 3 4c0-.6.4-1 1-1h3.5c.6 0 1 .4 1 1 0 1.3.2 2.5.6 3.6.1.3 0 .7-.2 1L6.6 10.8z"/>
        </svg>
        <span class="contact-phone">480-555-0147</span>
      </div>
    </footer>
  </main>
</body>
</html>
```